brindlewood carpentry business card 2.0

id like to get some extra info added to my current business card ,but i am also open to a new design as well ,id like it to be a clean professional look
i have attached the original card files, i have also attached the ridgemark guild logo and licensed builder logo that id like to add to all the current info on the old card
also the color green is important as seen in the company logo

Industry/Entity Type

Carpentry

Colors
9bcb3c

```html
<!DOCTYPE html>
<html lang="en">
<head>
<meta charset="utf-8">
<title>Brindlewood Carpentry – Business Card</title>
<link href="https://fonts.googleapis.com/css2?family=Open+Sans:wght@400;600&display=swap" rel="stylesheet">
<style>
  :root {
    --brand-green: #9bcb3c;
    --ink: #111111;
    --paper: #ffffff;
    --guild-navy: #1e3c7a;
  }
  * { margin: 0; padding: 0; box-sizing: border-box; }
  html, body {
    width: 1200px;
    height: 687px;
    overflow: hidden;
    background: var(--paper);
  }
  .card {
    position: relative;
    width: 1200px;
    height: 687px;
    background: var(--paper);
    font-family: "Open Sans", Arial, sans-serif;
    color: var(--ink);
  }
  .card-frame {
    position: absolute;
    left: 59px;
    top: 60px;
    width: 1084px;
    height: 569px;
    border: 6px solid var(--brand-green);
  }
  .badge-guild {
    position: absolute;
    left: 997px;
    top: 82px;
    width: 50px;
    height: 60px;
    background: var(--guild-navy);
  }
  .badge-licence {
    position: absolute;
    left: 1058px;
    top: 82px;
    width: 64px;
    height: 64px;
    border: 4px solid var(--brand-green);
    border-radius: 50%;
  }
  .wordmark {
    position: absolute;
    left: 0;
    width: 1200px;
    top: 180px;
    text-align: center;
    font-weight: 600;
    color: var(--ink);
    line-height: 1;
  }
  .wordmark-name {
    display: block;
    font-size: 78px;
    letter-spacing: 1px;
  }
  .wordmark-trade {
    display: block;
    margin-top: 20px;
    font-size: 48px;
    letter-spacing: 2px;
  }
  .person {
    position: absolute;
    right: 700px;
    top: 464px;
    text-align: right;
  }
  .person-name {
    font-size: 41px;
    font-weight: 400;
    line-height: 1;
    letter-spacing: 0.3px;
  }
  .person-role {
    margin-top: 10px;
    font-size: 24px;
    line-height: 1;
  }
  .divider {
    position: absolute;
    left: 599px;
    top: 444px;
    width: 4px;
    height: 114px;
    background: var(--ink);
  }
  .contact-list {
    position: absolute;
    left: 640px;
    top: 448px;
    list-style: none;
  }
  .contact-item {
    display: flex;
    align-items: center;
    height: 38px;
    font-size: 26px;
  }
  .contact-icon {
    width: 22px;
    height: 22px;
    margin-right: 37px;
    flex: none;
  }
</style>
</head>
<body>
  <main class="card">
    <div class="card-frame"></div>

    <div class="badge-guild" role="img" aria-label="Ridgemark Guild member badge"></div>
    <div class="badge-licence" role="img" aria-label="Licensed builder badge"></div>

    <h1 class="wordmark">
      <span class="wordmark-name">BRINDLEWOOD</span>
      <span class="wordmark-trade">CARPENTRY</span>
    </h1>

    <div class="person">
      <p class="person-name">DANIEL ARCHER</p>
      <p class="person-role">Director</p>
    </div>

    <div class="divider"></div>

    <ul class="contact-list">
      <li class="contact-item">
        <svg class="contact-icon" viewBox="0 0 24 24" aria-hidden="true">
          <path fill="#111" d="M6.6 2.5 9 5.6c.4.5.3 1.2-.1 1.6L7.4 8.6c.9 2.9 3.1 5.2 6 6.1l1.4-1.5c.4-.4 1.1-.5 1.6-.1l3.1 2.4c.5.4.6 1.1.2 1.6l-1.8 2.3c-.5.6-1.3.9-2.1.7C9 18.6 5.3 14.9 3.9 8.1c-.2-.8.1-1.6.7-2.1L6.6 2.5z"/>
        </svg>
        <span>02104518836</span>
      </li>
      <li class="contact-item">
        <svg class="contact-icon" viewBox="0 0 24 24" aria-hidden="true">
          <rect x="2" y="5" width="20" height="14" fill="none" stroke="#111" stroke-width="2"/>
          <path d="M2 5l10 8 10-8" fill="none" stroke="#111" stroke-width="2"/>
        </svg>
        <span>dan@brindlewoodcarpentry.co.nz</span>
      </li>
      <li class="contact-item">
        <svg class="contact-icon" viewBox="0 0 24 24" aria-hidden="true">
          <circle cx="12" cy="12" r="10" fill="#111"/>
          <g fill="none" stroke="#fff" stroke-width="1.4">
            <ellipse cx="12" cy="12" rx="4" ry="10"/>
            <line x1="2" y1="12" x2="22" y2="12"/>
            <line x1="12" y1="2" x2="12" y2="22"/>
          </g>
        </svg>
        <span>www.brindlewoodcarpentry.co.nz</span>
      </li>
    </ul>
  </main>
</body>
</html>
```